Korvell Plant Services

We are a heavy diesel mechanical business with additional air con certificates, remapping engine rebuilt

Contact Information for Business Card

Company Name, Director Name, Managing Director, Contact details, email and website

Font styles to use
Serif
Script

```html
<!DOCTYPE html>
<html lang="en">
<head>
<meta charset="utf-8">
<title>Korvell Plant Services – Business Card</title>
<link rel="stylesheet" href="https://fonts.googleapis.com/css2?family=Archivo:wght@400;500;800&family=Poppins:wght@300;400&display=swap">
<style>
  :root {
    --navy: #10107c;
    --navy-deep: #0b0b66;
    --ink: #111111;
    --text: #222222;
    --paper: #ffffff;
    --backdrop: #e4e4e4;
  }
  * { margin: 0; padding: 0; box-sizing: border-box; }
  html, body { width: 1200px; height: 900px; overflow: hidden; }
  body {
    background: var(--backdrop);
    font-family: "Archivo", Arial, sans-serif;
    position: relative;
  }
  .card {
    position: absolute;
    left: 250px;
    width: 700px;
    height: 400px;
    overflow: hidden;
    box-shadow: 0 6px 18px rgba(0,0,0,0.18);
  }
  /* Back side */
  .card--back { top: 30px; background: var(--navy); }
  .back-pattern {
    position: absolute; inset: 0;
    background: radial-gradient(circle at 60% 40%, #14148c 0%, var(--navy) 55%, var(--navy-deep) 100%);
  }
  .back-brand {
    position: absolute;
    left: 470px; top: 170px;
    display: flex; align-items: center; gap: 8px;
    color: var(--paper);
    font-weight: 800;
    font-size: 15px;
  }
  .brand-dot {
    width: 12px; height: 12px; border-radius: 50%;
    background: currentColor;
  }
  /* Front side */
  .card--front { top: 470px; background: var(--paper); }
  .front-brand {
    position: absolute;
    left: 48px; top: 50px;
    display: flex; align-items: center; gap: 14px;
    color: var(--navy);
    font-weight: 800;
    font-size: 34px;
    line-height: 1.05;
  }
  .front-brand .brand-dot { width: 30px; height: 30px; }
  .divider {
    position: absolute;
    left: 58px; right: 58px; top: 262px;
    height: 2px; background: var(--navy);
  }
  .person {
    position: absolute; right: 60px; top: 196px;
    text-align: right;
  }
  .person__name {
    color: var(--navy);
    font-weight: 800;
    font-size: 27px;
    letter-spacing: 0.5px;
    line-height: 1;
  }
  .person__role {
    font-family: "Poppins", Arial, sans-serif;
    font-size: 16px;
    color: var(--text);
    margin-top: 4px;
  }
  .contact {
    position: absolute; left: 60px; top: 272px;
    font-family: "Poppins", Arial, sans-serif;
    font-weight: 300;
    font-size: 17px;
    color: var(--text);
    list-style: none;
    line-height: 1.45;
  }
  .contact li { display: flex; align-items: center; gap: 8px; }
  .contact svg { width: 14px; height: 14px; flex: none; }
  .address {
    position: absolute; right: 60px; top: 280px;
    text-align: right;
    font-family: "Poppins", Arial, sans-serif;
    font-size: 17px;
    color: var(--text);
    line-height: 1.3;
    font-style: normal;
  }
  .footer-band { position: absolute; left: 0; bottom: 0; width: 700px; height: 74px; }
  .website {
    position: absolute; right: 56px; bottom: 11px;
    color: var(--paper);
    font-family: "Poppins", Arial, sans-serif;
    font-size: 16px;
    letter-spacing: 2px;
  }
</style>
</head>
<body>

<section class="card card--back" aria-label="Card back">
  <div class="back-pattern" role="img" aria-label="Repeating tone-on-tone brand pattern across the navy card back"></div>
  <div class="back-brand"><span class="brand-dot"></span>Korvell Plant Services</div>
</section>

<section class="card card--front" aria-label="Card front">
  <div class="front-brand"><span class="brand-dot"></span><span>Korvell<br>Plant Services</span></div>

  <div class="person">
    <div class="person__name">DEAN MARLOW</div>
    <div class="person__role">Director</div>
  </div>

  <div class="divider"></div>

  <ul class="contact">
    <li>
      <svg viewBox="0 0 16 16" aria-hidden="true"><path d="M4 1.5l2.2 3-1.3 1.6c.8 1.8 2.3 3.3 4.1 4.1l1.6-1.3 3 2.2-1.2 2.4C7 13.3 2.7 9 2.1 2.7z" fill="var(--navy)"/></svg>
      470-555-0182
    </li>
    <li>
      <svg viewBox="0 0 16 16" aria-hidden="true"><rect x="1.5" y="3.5" width="13" height="9" fill="none" stroke="var(--navy)" stroke-width="1.5"/><path d="M1.5 3.5l6.5 5 6.5-5" fill="none" stroke="var(--navy)" stroke-width="1.5"/></svg>
      info@korvellplantservices.com
    </li>
  </ul>

  <address class="address">2750 Halden Rd<br>Brookmere, GA 30099</address>

  <svg class="footer-band" viewBox="0 0 700 74" preserveAspectRatio="none" aria-hidden="true">
    <path d="M0 14 L345 30 Q352 31 360 33 L0 33 Z" fill="var(--ink)"/>
    <path d="M0 40 L345 52 Q370 34 400 34 L700 34 L700 74 L0 74 Z" fill="var(--navy)"/>
  </svg>
  <div class="website">www.korvellplantservices.com</div>
</section>

</body>
</html>
```